(3) Image Sliders for Wordpress Site

We need to update our WP slides on a corporate website. We are an IP communications solution provider to government and enterprises. Our website is www.velunor.com. You can see the existing sliders for size. I like crisp, professional-looking slides (NOT like the ones currently displayed). They shouldn't look like stock art/photos --- they should look original. They should also use current/new artistic methods (i.e. the "latest" concepts in design).

The Images should be JPG format, 946 x 376.

Use colors from logo on website, but don't completely restrict yourself. Photos are OK.

Slide Text:
Slide 1:
Main Message: "Creative solutions for government"
Bulleted text (use any kind of bullet or separator you want):
-Reduce FTE costs and eliminate capital expenses
-Dramatically improve community services
-Make government accessible for all constituents on all devices

Slide 2:
Main Message: "Corvane Systems Deployment"
-Take advantage of dramatic cost savings vs. going direct
-Leverage VeLUNOR's 13 years of experience
-Deploy On-Premises for optimal security, control and customization

Slide 3:
Main Message: "Enterprise Unified Communications"
-Revolutionize the way your people communicate and collaborate
-Realize instant cost savings by replacing multiple systems with one unified platform
-Bring everyone together, no matter where they are.

Hi Everyone I appreciate your submissions, but they are full of stock graphics and stuff I could have done..Looking for something more creative and unique to us. Since we're primarily a government/enterprise contractor, it doesn't have to be artsy or cute, but it does need to rise above the typical stock stuff i'm seeing. More information: -The Corvane Systems logo should go on the Corvane Systems-related slide -If you need more relevant logos or images let me know. Here are some slides that I like: http://brelmacraft.com/images/2014/0710-1/unslider.jpg http://brelmacraft.com/images/2014/0710-1/superslides.jpg http://www.tovelpikstudio.com/wp-content/uploads/2012/02/jquerysliders10b.jpg something like this with layered text for our gov slider, but NYC skyline: http://www.tovelpikstudio.com/wp-content/uploads/2012/02/jquerysliders18.jpg

Communications

```html
<!DOCTYPE html>
<html lang="en">
<head>
<meta charset="utf-8">
<title>Enterprise Unified Communications</title>
<link rel="stylesheet" href="https://fonts.googleapis.com/css2?family=Dosis:wght@400;500;600;700&display=swap">
<style>
  :root {
    --bg-light: #f7f7f7;
    --bg-mid: #e9e9e9;
    --ink: #1e1e1e;
    --text: #2b2b2b;
    --pink: #b5498c;
    --blue: #0aa6e3;
    --blue-deep: #0093d0;
    --orange: #f5a623;
    --green: #8cc63f;
    --brand: #1f3f8f;
    --dot: #d86a7f;
    --white: #ffffff;
  }
  * { margin: 0; padding: 0; box-sizing: border-box; }
  html, body { width: 1200px; height: 477px; overflow: hidden; }
  body { font-family: "Dosis", sans-serif; color: var(--text); }
  .slide {
    position: relative;
    width: 1200px;
    height: 477px;
    overflow: hidden;
    background: radial-gradient(ellipse at 50% 40%, var(--bg-light) 0%, var(--bg-mid) 100%);
  }
  .shapes { position: absolute; inset: 0; }
  .title {
    position: absolute;
    top: 38px;
    left: 0;
    width: 100%;
    text-align: center;
    font-size: 45px;
    font-weight: 500;
    letter-spacing: 0.5px;
    color: var(--ink);
  }
  .point {
    position: absolute;
    text-align: center;
    font-size: 28px;
    line-height: 37px;
    font-weight: 500;
  }
  .point strong { font-weight: 700; }
  .point--left { left: 93px; top: 245px; width: 220px; }
  .point--left strong { color: var(--pink); }
  .point--middle { left: 470px; top: 258px; width: 304px; }
  .point--middle strong { color: var(--blue); }
  .point--right { left: 880px; top: 160px; width: 260px; }
  .point--right strong { color: var(--green); }
  .brand {
    position: absolute;
    left: 342px;
    top: 218px;
    width: 132px;
    text-align: center;
    font-size: 27px;
    font-weight: 700;
    color: var(--brand);
    letter-spacing: 0.5px;
  }
</style>
</head>
<body>
<div class="slide">
  <svg class="shapes" width="1200" height="477" viewBox="0 0 1200 477" aria-hidden="true">
    <defs>
      <filter id="lift" x="-30%" y="-30%" width="160%" height="160%">
        <feDropShadow dx="0" dy="4" stdDeviation="7" flood-color="#000" flood-opacity="0.22"/>
      </filter>
      <radialGradient id="disc" cx="45%" cy="40%" r="65%">
        <stop offset="0%" stop-color="#ffffff"/>
        <stop offset="100%" stop-color="#ececec"/>
      </radialGradient>
    </defs>

    <!-- dotted orbit lines -->
    <circle class="orbit" cx="430" cy="330" r="200" fill="none" stroke="var(--dot)" stroke-width="1.6" stroke-dasharray="1.5 5" opacity="0.8"/>
    <circle class="orbit" cx="720" cy="420" r="250" fill="none" stroke="var(--dot)" stroke-width="1.6" stroke-dasharray="1.5 5" opacity="0.8"/>

    <!-- left disc -->
    <circle cx="203" cy="323" r="127" fill="url(#disc)" filter="url(#lift)"/>

    <!-- brand accent -->
    <circle cx="430" cy="300" r="70" fill="var(--orange)" filter="url(#lift)"/>
    <circle cx="408" cy="235" r="66" fill="url(#disc)" filter="url(#lift)"/>

    <!-- middle disc -->
    <circle cx="612" cy="382" r="178" fill="var(--blue)" filter="url(#lift)"/>
    <circle cx="624" cy="348" r="171" fill="url(#disc)" filter="url(#lift)"/>

    <!-- right disc -->
    <circle cx="984" cy="258" r="190" fill="var(--green)" filter="url(#lift)"/>
    <circle cx="1008" cy="226" r="165" fill="url(#disc)" filter="url(#lift)"/>

    <!-- network icon -->
    <g class="network-icon">
      <circle cx="1133" cy="362" r="53" fill="url(#disc)" filter="url(#lift)"/>
      <g stroke="#222" stroke-width="3" fill="none">
        <line x1="1133" y1="364" x2="1116" y2="345"/>
        <line x1="1133" y1="364" x2="1152" y2="352"/>
        <line x1="1133" y1="364" x2="1128" y2="386"/>
      </g>
      <g fill="#222">
        <circle cx="1133" cy="364" r="6"/>
        <circle cx="1116" cy="345" r="9"/>
        <circle cx="1152" cy="352" r="9"/>
        <circle cx="1128" cy="386" r="9"/>
      </g>
      <g fill="#fff">
        <circle cx="1116" cy="342.5" r="2.6"/><path d="M1111 350 a5 4 0 0 1 10 0z"/>
        <circle cx="1152" cy="349.5" r="2.6"/><path d="M1147 357 a5 4 0 0 1 10 0z"/>
        <circle cx="1128" cy="383.5" r="2.6"/><path d="M1123 391 a5 4 0 0 1 10 0z"/>
      </g>
    </g>
  </svg>

  <h1 class="title">ENTERPRISE UNIFIED COMMUNICATIONS</h1>

  <div class="brand">VeLUNOR</div>

  <p class="point point--left"><strong>Revolutionize</strong> the way your people communicate and collaborate</p>
  <p class="point point--middle"><strong>Realize instant cost savings</strong> by replacing multiple systems with one unified platform</p>
  <p class="point point--right"><strong>Bring everyone together,</strong> no matter where they are</p>
</div>
</body>
</html>
```